Brochure required

Looking at getting business brochure designed for my solar sales company. i will require a range of products to be listed on the brochure I require a simple/ elegent / professional looking brochure.

I am happy to provide designer with all the required information that must go into the brochure. otherwise please visit www.velkariston.com.au and view the products which i would like to allocate into the brochure aswell as our company logo and a little about me section

```html
<!DOCTYPE html>
<html lang="en">
<head>
<meta charset="utf-8">
<title>Products We Offer — Brochure Spread</title>
<link href="https://fonts.googleapis.com/css2?family=Open+Sans:wght@400;600;700&display=swap" rel="stylesheet">
<style>
  :root {
    --backdrop: #aaa7a5;
    --page-left: #ececec;
    --page-right: #f4f4f4;
    --title-blue: #1f78ad;
    --accent-teal: #1fa784;
    --body-text: #262626;
    --photo-sky: #5f9fdc;
    --photo-deep: #2b5fb4;
  }
  * { box-sizing: border-box; margin: 0; padding: 0; }
  html, body {
    width: 1200px; height: 900px; overflow: hidden;
    background: var(--backdrop);
    font-family: "Open Sans", Arial, sans-serif;
  }
  .spread {
    position: absolute; left: 59px; top: 67px;
    width: 1082px; height: 765px;
  }
  .page {
    position: absolute; top: 0; height: 765px; width: 541px;
  }
  .page--left {
    left: 0;
    background: linear-gradient(90deg, #f6f6f6 0%, var(--page-left) 70%, #e2e2e2 100%);
  }
  .page--right {
    left: 541px;
    background: linear-gradient(90deg, #f7f7f7 0%, var(--page-right) 100%);
  }
  .section-title {
    position: absolute; left: 24px; top: 31px;
    font-size: 21px; font-weight: 700; letter-spacing: 0.2px;
    color: var(--title-blue);
  }
  .title-rule {
    position: absolute; left: 256px; top: 36px; width: 808px; height: 12px;
  }
  .product-heading {
    position: absolute;
    font-size: 13px; font-weight: 700; color: var(--accent-teal);
  }
  .product-text {
    position: absolute;
    font-size: 11.4px; line-height: 16px; color: var(--body-text);
    text-align: justify; letter-spacing: 0;
  }
  .page--left .product-heading,
  .page--left .product-text { left: 25px; width: 481px; }
  .page--right .product-heading,
  .page--right .product-text { left: 28px; width: 491px; }
  .photo {
    position: absolute; top: 383px; height: 326px; width: 541px; left: 0;
  }
  .photo--field {
    background: linear-gradient(180deg, var(--photo-sky) 0%, #8fbde6 100%);
  }
  .photo--tracker {
    background: linear-gradient(180deg, var(--photo-deep) 0%, #4a87d2 100%);
  }
  .site-address {
    position: absolute; left: 0; width: 541px; top: 722px;
    text-align: center; font-size: 19px; color: #1e1e1e; letter-spacing: 0.2px;
  }
  .site-address .site-name { color: var(--accent-teal); font-weight: 600; }
</style>
</head>
<body>
  <main class="spread">
    <section class="page page--left">
      <h1 class="section-title">PRODUCTS WE OFFER</h1>

      <h2 class="product-heading" style="top:72px">Solar Inverters</h2>
      <p class="product-text" style="top:102px">The inverter is the heart of your solar power system. It’s primary functions are to convert the DC power from the panels into AC power for your home and to select the most productive operating voltage for the panels. Inverters come in a wide range of types, quality and sizes. The most common types of inverters are string inverters, which are mounted on your wall and connect to all the panels in your system.</p>
      <p class="product-text" style="top:213px">Another popular type is micro inverters, which are small inverters that sit under each panel. These inverters manage each panel individually, resulting in better yields, particularly on challenging roofs or systems subject to shading. Better quality inverters are available, and they come with longer warranties, better features, generate more power and are far more reliable. Better inverter manufacturers are also starting to introduce different connectivity options, online management portals, external devices (like consumption monitoring) and are now starting to include battery connectivity (Hybrid inverters). We have one of Australia’s largest selections of inverters and can recommend the perfect option for your solar project.</p>

      <div class="photo photo--field" role="img" aria-label="Photo: rows of ground-mounted solar panel arrays in a grassy field"></div>
    </section>

    <section class="page page--right">
      <h2 class="product-heading" style="top:72px">Solar Panels</h2>
      <p class="product-text" style="top:102px">Velkariston has partnered with the most reputable solar PV manufacturers in the world to offer you the best solar panels on the market. We have selected high-end PV modules with the best track records to ensure we supply top-quality products to our customers. Whether you are looking to buy solar panels for residential or commercial use, look no further: Velkariston provides superior solar panels for home and business purposes, sourced from trusted tier-1 manufacturers, as well as premium-brand solar power inverters.</p>

      <h2 class="product-heading" style="top:241px">Solar Batteries</h2>
      <p class="product-text" style="top:271px">Energy storage systems are now a reality, and homes like yours is where it begins. In the next few years, we will see a fundamental shift in the way all energy users meet their energy requirements and how utility providers integrate with storage systems. For home owners, they can benefit right now from energy storage in a variety of ways.</p>

      <div class="photo photo--tracker" role="img" aria-label="Photo: a single pole-mounted solar tracker array"></div>

      <p class="site-address">www.<span class="site-name">velkariston</span>.com.au</p>
    </section>

    <svg class="title-rule" viewBox="0 0 808 12" aria-hidden="true">
      <line x1="6" y1="6" x2="802" y2="6" stroke="#1fa784" stroke-width="2"/>
      <circle cx="6" cy="6" r="5" fill="#1fa784"/>
      <circle cx="802" cy="6" r="5" fill="#1fa784"/>
    </svg>
  </main>
</body>
</html>
```